Marrow Business Cards

Front of business card will have logo, name, address, & telephone number. Back of card will have a list of services provided - Roads, Substation Pads, Temporary Pads, Site Pads, Land Leveling, Powerline Row Cleaning, Land Clearing, Gates, Fencing, Construction Entrances, Excavation, Trenching, Underground Utilities, Directional Boring, Pile Driving. We are a construction company that uses heavy equipment like bulldozers, motor graders/blades, dump trucks, backhoes, hydro axes, & skid loaders. We build roads, pads, & install electric utility lines & waterlines underground. This logo is new. The word "Construction" can be smaller as uploaded 2 example edited logos. We will be using this card design for many employees.
Target Market(s)
Industrial Electric Powerline, Wind Turbine, Solar Panel, & Water Utility companies.
Contact Information for Business Card
Name/Position - Dorian Quale - Owner
Address: 4837 FM 582
Merkel, TX 79418
Phone number - (325) 418-2906

```html
<!DOCTYPE html>
<html lang="en">
<head>
<meta charset="utf-8">
<title>Marrow Construction – Business Cards</title>
<link rel="stylesheet" href="https://fonts.googleapis.com/css2?family=Montserrat:wght@400;500;600;700&display=swap">
<style>
  :root {
    --page: #e9e7e6;
    --card-white: #fbfaf9;
    --maroon: #6a1f2d;
    --maroon-back: #5b1b26;
    --maroon-band: #47131c;
    --cream: #efe8e6;
    --grey: #8a8587;
  }
  * { box-sizing: border-box; margin: 0; padding: 0; }
  html, body {
    width: 1200px; height: 900px; overflow: hidden;
    background: var(--page);
    font-family: "Montserrat", sans-serif;
  }
  .sheet {
    width: 1200px; height: 900px;
    display: flex; align-items: center; justify-content: center; gap: 56px;
  }
  .card {
    width: 500px; height: 286px;
    border-radius: 4px;
    box-shadow: 0 10px 28px rgba(0,0,0,.18);
    position: relative; overflow: hidden;
    display: flex; flex-direction: column; align-items: center;
  }
  .wordmark {
    display: flex; align-items: center; gap: 10px;
    font-size: 26px; font-weight: 600; letter-spacing: .05em;
    text-transform: uppercase; white-space: nowrap;
  }
  .wordmark__mark { width: 14px; height: 14px; background: currentColor; flex: none; }

  /* Front */
  .card--front { background: var(--card-white); color: var(--maroon); padding-top: 46px; }
  .person__name { margin-top: 24px; font-size: 17px; font-weight: 400; letter-spacing: .16em; text-transform: uppercase; }
  .person__role { margin-top: 2px; font-size: 13px; color: var(--grey); letter-spacing: .04em; }
  .divider { width: 12px; height: 2px; background: var(--maroon); margin: 12px 0; }
  .contact { font-style: normal; text-align: center; font-size: 15px; line-height: 1.35; letter-spacing: .03em; font-weight: 500; }

  /* Back */
  .card--back { background: var(--maroon-back); color: var(--cream); padding-top: 52px; }
  .services {
    position: absolute; left: 0; right: 0; bottom: 30px;
    background: var(--maroon-band);
    padding: 14px 16px 16px; text-align: center;
  }
  .services__title { font-size: 11px; font-weight: 700; letter-spacing: .12em; margin-bottom: 6px; }
  .services__list { list-style: none; font-size: 9px; font-weight: 500; letter-spacing: .05em; line-height: 1.65; white-space: nowrap; }
</style>
</head>
<body>
<main class="sheet">
  <section class="card card--front" aria-label="Business card front">
    <div class="wordmark"><span class="wordmark__mark"></span>Marrow Construction</div>
    <p class="person__name">Dorian Quale</p>
    <p class="person__role">Owner</p>
    <span class="divider"></span>
    <address class="contact">
      (471) 418-2906<br>
      4837 FM 582 Calloway<br>
      TX 79418
    </address>
  </section>

  <section class="card card--back" aria-label="Business card back">
    <div class="wordmark"><span class="wordmark__mark"></span>Marrow Construction</div>
    <div class="services">
      <p class="services__title">OUR SERVICES</p>
      <ul class="services__list">
        <li>ROADS | SUBSTATION PADS | TEMPORARY PADS | SITE PADS | LAND LEVELING</li>
        <li>POWERLINE ROW CLEANING | GATES | FENCING | CONSTRUCTION ENTRANCES</li>
        <li>EXCAVATION | TRENCHING | UNDERGROUND UTILITIES</li>
        <li>DIRECTIONAL BORING | PILE DRIVING | LAND CLEARING</li>
      </ul>
    </div>
  </section>
</main>
</body>
</html>
```